Media Broker Web design

Re-design a website for an independant media buying and planning marketing business in Australia. We develop unique marketing plans for small to medium businesses. NFP's are our sweet spot. We tailor a strategy that takes account of business needs, whilst respecting the brand footprint. Using an innovative and purpose-built media buying platform, we access the best media houses to directly understand availability, and then negotiate the most competitive rates to maximise campaign results and ensure a superior ROI. The current website is not engaging, or very interactive. We are looking at something more inspiring that builds confidence in our business and the work that we do in assisting others to market themselves. We want something clean & simple, engaging, customer centric, easy to navigate, including customer logo's and testimonials. See attached logo and colours - the grey & orange. We ignite brands with performance driven media buying. "You talk, we listen"
Updates

Need extra days to review

Target Market(s)

Companies seeking support with marketing campaigns

Industry/Entity Type

Media

Number of Pages Required

3 page

Colors
F0912C
F2A743
F7CA91
FBE8D2
FDF5EE

Requirements
Must have
• About us, Services offered, contact us, current clients, testimonials
Nice to have
• Team photo

```html
<!DOCTYPE html>
<html lang="en">
<head>
<meta charset="utf-8">
<title>Signal Media Partners</title>
<link href="https://fonts.googleapis.com/css2?family=Fira+Sans:wght@400;500;600;700&family=Fira+Sans+Condensed:wght@600;700;800&display=swap" rel="stylesheet">
<style>
:root{
  --orange:#F0912C;
  --orange-2:#F2A743;
  --orange-3:#F7CA91;
  --orange-4:#FBE8D2;
  --orange-5:#FDF5EE;
  --ink:#1f1f1f;
  --text:#333;
  --grey:#5a5a5a;
  --dark:#333333;
  --light:#f1f1f1;
  --white:#fff;
}
*{margin:0;padding:0;box-sizing:border-box}
html,body{width:1200px;height:3750px;overflow:hidden}
body{position:relative;background:var(--white);font-family:"Fira Sans",Arial,sans-serif;color:var(--text)}
.abs{position:absolute}
.head{font-family:"Fira Sans Condensed","Arial Narrow",sans-serif;font-weight:700;color:var(--ink);text-transform:uppercase}
.brand{font-family:"Fira Sans",Arial,sans-serif;font-weight:600;color:var(--grey);display:flex;align-items:center;gap:10px}
.brand .dot{width:22px;height:22px;border-radius:50%;background:var(--orange)}

/* header */
.site-header{left:0;top:0;width:1200px;height:112px;border-bottom:1px solid #e3e3e3;background:var(--white)}
.site-header .brand{left:172px;top:38px;font-size:24px}
.contact-top{right:172px;top:24px;display:flex;gap:18px;font-size:15px;font-weight:500;color:var(--ink);align-items:center}
.contact-top span{display:flex;align-items:center;gap:10px}
.ico-circle{width:30px;height:30px;border-radius:50%;background:var(--orange);display:flex;align-items:center;justify-content:center}
.main-nav{right:172px;top:76px;display:flex;gap:20px;font-size:15px;font-weight:600;color:var(--ink)}

/* hero */
.hero{left:0;top:113px;width:1200px;height:618px;background:linear-gradient(180deg,#fafafa,#eeeeee)}
.hero-photo{left:655px;top:0;width:545px;height:600px;background:linear-gradient(180deg,#e7f1f4 0%,#f4f4f4 45%,#c9c9c9 100%)}
.hero-shade{left:0;top:570px;width:1200px;height:48px;background:linear-gradient(180deg,rgba(0,0,0,0),rgba(0,0,0,.12))}
.hero-panel{left:135px;top:97px;width:458px;height:425px}
.hero-copy{left:170px;top:140px;width:400px}
.hero-copy h1{font-size:41px;line-height:44px;letter-spacing:.3px}
.hero-copy p{margin-top:20px;font-size:23px;line-height:30px;color:var(--ink);font-weight:500}
.btn{display:inline-block;margin-top:26px;background:var(--white);color:var(--ink);font-weight:600;font-size:17px;padding:12px 20px;border-radius:24px}
.dots{margin-top:30px;display:flex;gap:9px}
.dots i{width:12px;height:12px;border-radius:50%;background:var(--white)}

/* about */
.about-art{left:55px;top:795px;width:450px;height:400px;border-radius:50% 50% 40% 40%;background:radial-gradient(circle at 45% 40%,var(--orange-2) 0%,var(--orange-3) 30%,#dcdcf7 58%,rgba(255,255,255,0) 72%)}
.about-copy{left:548px;top:812px;width:480px}
.about-copy h2{font-size:31px}
.about-copy h3{font-family:"Fira Sans Condensed",sans-serif;font-weight:600;font-size:22px;color:var(--ink);margin-top:2px;text-transform:uppercase}
.about-copy p{font-size:13.5px;line-height:22.5px;text-align:justify;color:var(--ink);margin-top:16px}
.about-copy p+p{margin-top:22px}

/* steps */
.steps{left:0;top:1263px;width:1200px;height:610px;background:linear-gradient(180deg,#f0f0f0,#f7f7f7 50%,#ececec)}
.steps h2{position:absolute;left:0;width:1200px;top:50px;text-align:center;font-size:31px}
.step{top:190px;width:273px;height:370px;background:var(--white);border-radius:26px;text-align:center;padding:70px 14px 0}
.step .badge{position:absolute;left:76px;top:-62px;width:121px;height:121px;border-radius:50%;background:var(--white);display:flex;align-items:center;justify-content:center}
.step .badge div{width:106px;height:106px;border-radius:50%;background:var(--orange);display:flex;align-items:center;justify-content:center}
.step h4{font-family:"Fira Sans Condensed",sans-serif;font-weight:600;font-size:20px;color:var(--ink);text-transform:uppercase}
.step h3{font-size:27px;line-height:28px}
.step p{font-size:12px;line-height:22.5px;color:var(--ink);margin-top:14px}
.step.featured{background:var(--orange)}
.step.featured .badge div{background:var(--white)}

/* services */
.services-title{left:172px;top:1942px;font-size:31px}
.service{left:172px;width:440px;height:70px}
.service .ring{position:absolute;left:0;top:2px;width:64px;height:64px;border-radius:50%;border:3px solid var(--orange);display:flex;align-items:center;justify-content:center}
.service .ring div{width:52px;height:52px;border-radius:50%;background:var(--orange);display:flex;align-items:center;justify-content:center}
.service .ring.grey{border-color:#555}
.service .ring.grey div{background:#555}
.service h3{position:absolute;left:78px;top:0;font-size:22px}
.service p{position:absolute;left:78px;top:30px;width:360px;font-size:12px;line-height:22px;color:var(--ink)}
.services-art{left:630px;top:1935px;width:530px;height:460px;border-radius:40px;background:radial-gradient(circle at 55% 50%,var(--orange-3) 0%,var(--orange-4) 35%,#eef4f6 60%,rgba(255,255,255,0) 75%)}

/* clients */
.clients{left:0;top:2465px;width:1200px;height:357px;background:linear-gradient(180deg,var(--orange) 0%,var(--orange-2) 55%,var(--orange) 100%)}
.clients h2{position:absolute;top:80px;width:1200px;text-align:center;font-size:31px}
.client{top:147px;width:273px;height:136px;background:var(--white);border-radius:22px;display:flex;align-items:center;justify-content:center}
.client .brand{font-size:40px;color:#2b2b3a;font-weight:500}
.client .brand .dot{width:34px;height:34px}

/* testimonials */
.testi-title{left:0;top:2890px;width:1200px;text-align:center;font-size:31px}
.bubble{top:2975px;width:423px;height:300px}
.bubble .inner{position:absolute;left:0;top:0;width:423px;height:232px;padding:40px 22px 0;text-align:center}
.stars{display:flex;justify-content:center;gap:5px}
.bubble h3{font-size:33px;margin-top:10px}
.bubble p{font-size:12.5px;line-height:22.5px;color:var(--ink);margin-top:6px}
.bubble .who{position:absolute;top:310px;font-size:19px;font-weight:500;color:var(--ink)}

/* footer */
.site-footer{left:0;top:3368px;width:1200px;height:382px;background:var(--dark);color:var(--white)}
.foot-logo{left:172px;top:91px;width:243px;height:142px;background:var(--white);border-radius:24px;display:flex;align-items:center;justify-content:center}
.foot-logo .brand{font-size:21px}
.foot-nav{left:490px;top:86px;font-size:15px;font-weight:600;line-height:33px}
.foot-contact{left:720px;top:92px;font-size:15px;font-weight:600}
.foot-contact .row{display:flex;align-items:center;gap:12px;height:30px;margin-bottom:16px}
.foot-contact .ico-circle{background:var(--white)}
.foot-contact .cities{margin-left:42px;line-height:27px}
.foot-rule{left:172px;top:312px;width:856px;height:1px;background:#8a8a8a}
.copyright{left:0;top:336px;width:1200px;text-align:center;font-size:15px;font-weight:600}
</style>
</head>
<body>

<header class="site-header abs">
  <div class="brand abs"><i class="dot"></i>Signal Media Partners</div>
  <div class="contact-top abs">
    <span><b class="ico-circle"><svg width="14" height="11" viewBox="0 0 14 11"><rect x="1" y="1" width="12" height="9" fill="none" stroke="#fff" stroke-width="1.6"/><path d="M1 1l6 5 6-5" fill="none" stroke="#fff" stroke-width="1.6"/></svg></b>hello@signalmediapartners.com.au</span>
    <span><b class="ico-circle"><svg width="14" height="14" viewBox="0 0 24 24"><path d="M6.6 10.8a15 15 0 006.6 6.6l2.2-2.2a1 1 0 011-.25 11 11 0 003.5.56 1 1 0 011 1V20a1 1 0 01-1 1A17 17 0 013 4a1 1 0 011-1h3.5a1 1 0 011 1c0 1.25.2 2.45.56 3.57a1 1 0 01-.25 1z" fill="#fff"/></svg></b>0400 123 987</span>
  </div>
  <nav class="main-nav abs"><span>HOME</span><span>ABOUT US</span><span>SERVICES OFFERED</span><span>CONTACT US</span><span>CURRENT CLIENTS</span></nav>
</header>

<section class="hero abs">
  <div class="hero-photo abs" role="img" aria-label="Business team standing in a line using phones beneath a wall of hand-drawn marketing icons"></div>
  <div class="hero-shade abs"></div>
  <svg class="hero-panel abs" viewBox="0 0 458 425"><polygon points="0,0 458,0 348,425 0,425" fill="#F0912C"/></svg>
  <div class="hero-copy abs">
    <h1 class="head">Independent media planning &amp; buying specialists</h1>
    <p>We’re obsessed with supporting your success</p>
    <span class="btn">READ MORE</span>
    <div class="dots"><i></i><i></i><i></i></div>
  </div>
</section>

<div class="about-art abs" role="img" aria-label="Illustration of people assembling puzzle pieces on a giant light bulb"></div>
<section class="about-copy abs">
  <h2 class="head">About us</h2>
  <h3>You talk, we listen (and deliver)</h3>
  <p>Leverage the expertise of SMP’s award-winning media specialists and ignite your brand. With reach across every medium nationally, and offices in Brisbane, the Goldy and Sunshine Coast, we have you covered!</p>
  <p>SMP are a media planning and buying team like no other. Through our team of industry leading professionals, you gain access to a broad range of experience in local, national, and international brands.<br>Our team offer decades of knowledge relating to media strategy, planning, and buying across the complete spectrum of sectors and platforms nationwide.<br>Our team offer decades of knowledge relating to media strategy, planning, and buying across the complete spectrum of sectors and platforms nationwide.</p>
</section>

<section class="steps abs">
  <h2 class="head">Easy to do business with</h2>
  <div class="step abs" style="left:172px">
    <div class="badge"><div><svg width="54" height="54" viewBox="0 0 54 54" fill="none" stroke="#222" stroke-width="3"><circle cx="13" cy="12" r="6"/><circle cx="27" cy="10" r="6"/><circle cx="41" cy="12" r="6"/><path d="M5 48V30a6 6 0 016-6h4M49 48V30a6 6 0 00-6-6h-4M19 48V28a6 6 0 016-6h4a6 6 0 016 6v20"/></svg></div></div>
    <h4>Step 1</h4><h3 class="head">Meet us</h3>
    <p>We genuinely love to hear your storey – it’s just inherent in our DNA. When we meet, maybe over coffee (or a hot choccy – we don’t judge), our senior professionals will listen to understand your organisations objectives and share with you our strategic insights so that you may choose whether we are the right partner for you to collaborate with.</p>
  </div>
  <div class="step featured abs" style="left:464px">
    <div class="badge"><div><svg width="54" height="58" viewBox="0 0 54 58" fill="none" stroke="#222" stroke-width="3"><rect x="8" y="8" width="32" height="42" rx="3"/><rect x="17" y="3" width="14" height="8" rx="2"/><path d="M15 22h18M15 30h18M15 38h10"/><circle cx="40" cy="46" r="9" fill="#222"/><path d="M36 46l3 3 5-6" stroke="#fff"/></svg></div></div>
    <h4>Step 2</h4><h3 class="head">Work with us</h3>
    <p>If we both agree that it’s meant to be, then we will develop a unique marketing plan for you. We will tailor a strategy that takes account of your needs, and that the long-term outcome is one you are excited for. We clearly detail costings and never lock clients into binding contracts.</p>
  </div>
  <div class="step abs" style="left:755px">
    <div class="badge"><div><svg width="54" height="58" viewBox="0 0 54 58" fill="none" stroke="#222" stroke-width="3"><path d="M27 4l4 9 10 1-7 7 2 10-9-5-9 5 2-10-7-7 10-1z" fill="#222"/><path d="M25 30v16l-4-3-3 3 7 9h14l4-14-11-3v-8z"/></svg></div></div>
    <h4>Step 3</h4><h3 class="head">Celebrate with us</h3>
    <p>SMP take great pride in the results we generate for our clients. With personal engagement from the top down, our Agency Director works with you directly to ensure that we consistently deliver on your goals, because with SMP, its personal.</p>
  </div>
</section>

<h2 class="services-title head abs">Services offered</h2>
<div class="service abs" style="top:2010px">
  <div class="ring"><div><svg width="26" height="24" viewBox="0 0 26 24" fill="none" stroke="#222" stroke-width="2.2"><rect x="2" y="6" width="22" height="16" rx="2"/><path d="M9 1l4 5 4-5"/><path d="M11 11v7l6-3.5z" fill="#222"/></svg></div></div>
  <h3 class="head">Television &amp; radio</h3><p>Whether it’s a local or national campaign, branding or call to action, we use our expertise.</p>
</div>
<div class="service abs" style="top:2108px">
  <div class="ring grey"><div><svg width="26" height="24" viewBox="0 0 26 24" fill="none" stroke="#fff" stroke-width="2.2"><path d="M2 11L13 2l11 9v11H2z"/><path d="M8 22v-8h10v8"/></svg></div></div>
  <h3 class="head">Out of home</h3><p>Whether it’s a local or national campaign, branding or call to action, we use our expertise.</p>
</div>
<div class="service abs" style="top:2206px">
  <div class="ring"><div><svg width="26" height="24" viewBox="0 0 26 24" fill="none" stroke="#222" stroke-width="2.2"><rect x="7" y="2" width="12" height="6"/><rect x="2" y="8" width="22" height="10" rx="2"/><rect x="7" y="14" width="12" height="8" fill="#F0912C"/></svg></div></div>
  <h3 class="head">Print &amp; digital</h3><p>Whether it’s a local or national campaign, branding or call to action, we use our expertise.</p>
</div>
<div class="service abs" style="top:2304px">
  <div class="ring grey"><div><svg width="26" height="24" viewBox="0 0 26 24" fill="none" stroke="#fff" stroke-width="2.2"><rect x="2" y="3" width="20" height="16" rx="2"/><path d="M2 8h20"/><path d="M9 11v6l5-3z" fill="#fff"/><circle cx="21" cy="19" r="3.5"/></svg></div></div>
  <h3 class="head">Creative &amp; production</h3><p>Whether it’s a local or national campaign, branding or call to action, we use our expertise.</p>
</div>
<div class="services-art abs" role="img" aria-label="Illustration of a person with a laptop and megaphone surrounded by digital marketing symbols"></div>

<section class="clients abs">
  <h2 class="head">Current clients</h2>
  <div class="client abs" style="left:172px"><span class="brand"><i class="dot"></i>Norvale</span></div>
  <div class="client abs" style="left:464px"><span class="brand"><i class="dot"></i>Loopfield</span></div>
  <div class="client abs" style="left:755px"><span class="brand"><i class="dot"></i>Kestra</span></div>
</section>

<h2 class="testi-title head abs">Testimonials</h2>
<div class="bubble abs" style="left:172px">
  <svg class="abs" width="423" height="300" viewBox="0 0 423 300"><path d="M40 0H383a40 40 0 0140 40V192a40 40 0 01-40 40H320L288 290l8-58H40A40 40 0 010 192V40A40 40 0 0140 0z" fill="#fff" stroke="#e4e4e4" stroke-width="2"/></svg>
  <div class="inner">
    <div class="stars"><svg width="130" height="24" viewBox="0 0 130 24"><g fill="#F0912C"><path id="st" d="M12 1l3.3 7 7.7.9-5.7 5.2 1.6 7.6L12 17.8 5.1 21.7l1.6-7.6L1 8.9 8.7 8z"/><use href="#st" x="26"/><use href="#st" x="52"/><use href="#st" x="78"/></g><use href="#st" x="104" fill="none" stroke="#333" stroke-width="1.4"/></svg></div>
    <h3 class="head">Good support</h3>
    <p>Duis aute irure dolor in reprehenderit in voluptate velit esse cillum dolore eu fugiat nulla pariatur. Excepteur sint occaecat cupidatat non proident, sunt in culpa qui officia deserunt mollit anim id est laborum.</p>
  </div>
  <span class="who" style="left:220px">Liam Porter</span>
</div>
<div class="bubble abs" style="left:606px">
  <svg class="abs" width="423" height="300" viewBox="0 0 423 300"><path d="M40 0H383a40 40 0 0140 40V192a40 40 0 01-40 40H320L288 290l8-58H40A40 40 0 010 192V40A40 40 0 0140 0z" fill="#fff" stroke="#e4e4e4" stroke-width="2"/></svg>
  <div class="inner">
    <div class="stars"><svg width="130" height="24" viewBox="0 0 130 24"><g fill="#F0912C"><path id="st2" d="M12 1l3.3 7 7.7.9-5.7 5.2 1.6 7.6L12 17.8 5.1 21.7l1.6-7.6L1 8.9 8.7 8z"/><use href="#st2" x="26"/><use href="#st2" x="52"/><use href="#st2" x="78"/></g><use href="#st2" x="104" fill="none" stroke="#333" stroke-width="1.4"/></svg></div>
    <h3 class="head">Good support</h3>
    <p>Duis aute irure dolor in reprehenderit in voluptate velit esse cillum dolore eu fugiat nulla pariatur. Excepteur sint occaecat cupidatat non proident, sunt in culpa qui officia deserunt mollit anim id est laborum.</p>
  </div>
  <span class="who" style="left:232px">Hayes</span>
</div>

<footer class="site-footer abs">
  <div class="foot-logo abs"><span class="brand"><i class="dot"></i>Signal Media Partners</span></div>
  <nav class="foot-nav abs"><div>HOME</div><div>ABOUT US</div><div>SERVICES OFFERED</div><div>CONTACT US</div><div>CURRENT CLIENTS</div></nav>
  <div class="foot-contact abs">
    <div class="row"><b class="ico-circle"><svg width="14" height="11" viewBox="0 0 14 11"><rect x="1" y="1" width="12" height="9" fill="none" stroke="#333" stroke-width="1.6"/><path d="M1 1l6 5 6-5" fill="none" stroke="#333" stroke-width="1.6"/></svg></b>hello@signalmediapartners.com.au</div>
    <div class="row"><b class="ico-circle"><svg width="14" height="14" viewBox="0 0 24 24"><path d="M6.6 10.8a15 15 0 006.6 6.6l2.2-2.2a1 1 0 011-.25 11 11 0 003.5.56 1 1 0 011 1V20a1 1 0 01-1 1A17 17 0 013 4a1 1 0 011-1h3.5a1 1 0 011 1c0 1.25.2 2.45.56 3.57a1 1 0 01-.25 1z" fill="#333"/></svg></b>0400 123 987</div>
    <div class="cities">BRISBANE<br>GOLD COAST<br>SUNSHINE COAST</div>
  </div>
  <div class="foot-rule abs"></div>
  <div class="copyright abs">Copyrights @ 2024 Signal Media Partners.</div>
</footer>

</body>
</html>
```